Tidal Fern Business Cards

We need something new, fun and exciting for business cards. Our current ones are just plain and we need a design that pops. We want name, position held, phone, email on the front, and a 20% discount on the back. I have also uploaded our old business cards creative to see what we are not wanting, and how boring they were and we want something jazzed up from this, cool design and catches people attention.

```html
<!DOCTYPE html>
<html lang="en">
<head>
<meta charset="UTF-8">
<title>Tidal Fern Business Cards</title>
<link href="https://fonts.googleapis.com/css2?family=Montserrat:wght@300;400;600;700;800&family=Open+Sans:wght@400;600&display=swap" rel="stylesheet">
<style>
  :root {
    --navy: #1d3d6e;
    --coral: #ee6a6a;
    --white: #ffffff;
    --backdrop: #8c877f;
    --shadow: rgba(0, 0, 0, 0.35);
  }
  * { box-sizing: border-box; margin: 0; padding: 0; }
  html, body {
    width: 1200px; height: 900px; overflow: hidden;
    background: var(--backdrop);
  }
  .stage { position: relative; width: 1200px; height: 900px; }

  .card {
    position: absolute; top: 120px;
    width: 380px; height: 640px;
    background: var(--white);
    box-shadow: 0 18px 40px var(--shadow);
    overflow: hidden;
  }
  .card--back { left: 170px; }
  .card--front { left: 650px; }

  .tab { position: absolute; display: block; z-index: 2; }
  .tab--navy { background: var(--navy); }
  .tab--coral { background: var(--coral); }
  .tab--side { width: 12px; height: 44px; }
  .tab--edge { width: 44px; height: 12px; }

  .brand {
    position: absolute; left: 0; right: 0; top: 70px;
    display: flex; flex-direction: column; align-items: center; gap: 16px;
  }
  .card--front .brand { top: 46px; }
  .brand__dot {
    width: 56px; height: 56px; border-radius: 50%;
    background: var(--coral);
  }
  .brand__name {
    font-family: "Montserrat", sans-serif;
    font-weight: 700; font-size: 46px; letter-spacing: -0.5px;
    color: var(--navy); line-height: 1.1;
  }

  .offer {
    position: absolute; left: 50%; top: 360px;
    width: 210px; height: 210px; margin-left: -105px;
    border-radius: 50%;
    border: 4px solid;
    border-color: var(--coral) var(--navy) var(--coral) var(--navy);
    display: flex; flex-direction: column; align-items: center; justify-content: center;
    font-family: "Montserrat", sans-serif; font-weight: 800;
    color: var(--navy); line-height: 0.95;
  }
  .offer__value, .offer__label { font-size: 60px; }

  .card__panel {
    position: absolute; left: 0; right: 0; top: 220px; bottom: 0;
    background: var(--navy);
  }
  .person {
    position: absolute; left: 0; right: 0; top: 20px; text-align: center;
    font-family: "Montserrat", sans-serif; color: var(--white);
  }
  .person__name { font-size: 24px; font-weight: 300; line-height: 1.2; }
  .person__name strong { font-weight: 700; }
  .person__role { font-size: 15px; font-weight: 300; margin-top: 2px; }

  .contact {
    position: absolute; left: 70px; width: 240px; height: 70px;
    border: 1.5px solid var(--coral);
    display: flex; flex-direction: column; align-items: center; justify-content: center;
    font-family: "Open Sans", sans-serif; font-size: 13px; line-height: 1.45;
    color: var(--white); text-align: center; padding-top: 8px;
  }
  .contact--address { top: 110px; }
  .contact--phone { top: 220px; }
  .contact--email { top: 330px; }
  .contact__icon {
    position: absolute; top: -17px; left: 50%; margin-left: -17px;
    width: 34px; height: 34px; border-radius: 50%;
    background: var(--coral);
    display: flex; align-items: center; justify-content: center;
  }
</style>
</head>
<body>
<main class="stage">

  <section class="card card--back" aria-label="Card back with discount">
    <span class="tab tab--side tab--navy" style="left:0;top:40px"></span>
    <span class="tab tab--side tab--coral" style="left:0;top:200px"></span>
    <span class="tab tab--side tab--navy" style="left:0;top:360px"></span>
    <span class="tab tab--side tab--coral" style="left:0;top:520px"></span>
    <span class="tab tab--side tab--coral" style="right:0;top:40px"></span>
    <span class="tab tab--side tab--navy" style="right:0;top:200px"></span>
    <span class="tab tab--side tab--coral" style="right:0;top:360px"></span>
    <span class="tab tab--side tab--navy" style="right:0;top:520px"></span>
    <span class="tab tab--edge tab--navy" style="left:40px;top:0"></span>
    <span class="tab tab--edge tab--coral" style="right:40px;top:0"></span>
    <span class="tab tab--edge tab--coral" style="left:40px;bottom:0"></span>
    <span class="tab tab--edge tab--navy" style="right:40px;bottom:0"></span>

    <div class="brand">
      <span class="brand__dot"></span>
      <span class="brand__name">Tidal Fern</span>
    </div>

    <div class="offer">
      <span class="offer__value">20%</span>
      <span class="offer__label">OFF</span>
    </div>
  </section>

  <section class="card card--front" aria-label="Card front with contact details">
    <div class="brand">
      <span class="brand__dot"></span>
      <span class="brand__name">Tidal Fern</span>
    </div>

    <div class="card__panel">
      <div class="person">
        <p class="person__name"><strong>Lorem</strong> ipsum</p>
        <p class="person__role">Designer</p>
      </div>

      <div class="contact contact--address">
        <span class="contact__icon">
          <svg width="18" height="18" viewBox="0 0 24 24" fill="#fff"><path d="M12 3 2 12h3v8h5v-5h4v5h5v-8h3z"/></svg>
        </span>
        <p>Street Address Here<br>Italy, 2222</p>
      </div>

      <div class="contact contact--phone">
        <span class="contact__icon">
          <svg width="18" height="18" viewBox="0 0 24 24" fill="#fff"><path d="M6.6 10.8a15 15 0 0 0 6.6 6.6l2.2-2.2c.3-.3.7-.4 1-.2 1.1.4 2.3.6 3.6.6.6 0 1 .4 1 1V20c0 .6-.4 1-1 1A17 17 0 0 1 3 4c0-.6.4-1 1-1h3.5c.6 0 1 .4 1 1 0 1.3.2 2.5.6 3.6.1.3 0 .7-.2 1z"/></svg>
        </span>
        <p>+77 7777 7777 7777<br>+66 6666 6666 6666</p>
      </div>

      <div class="contact contact--email">
        <span class="contact__icon">
          <svg width="18" height="18" viewBox="0 0 24 24" fill="#fff"><path d="M2 11 22 3l-6 18-4-7z"/></svg>
        </span>
        <p>username@email.com</p>
      </div>
    </div>

    <span class="tab tab--side tab--navy" style="left:0;top:30px"></span>
    <span class="tab tab--side tab--coral" style="left:0;top:170px"></span>
    <span class="tab tab--side tab--coral" style="left:0;top:330px"></span>
    <span class="tab tab--side tab--coral" style="left:0;top:520px"></span>
    <span class="tab tab--side tab--coral" style="right:0;top:30px"></span>
    <span class="tab tab--side tab--coral" style="right:0;top:200px"></span>
    <span class="tab tab--side tab--coral" style="right:0;top:400px"></span>
    <span class="tab tab--side tab--coral" style="right:0;top:560px"></span>
    <span class="tab tab--edge tab--navy" style="left:40px;top:0"></span>
    <span class="tab tab--edge tab--coral" style="right:40px;top:0"></span>
    <span class="tab tab--edge tab--coral" style="left:40px;bottom:0"></span>
    <span class="tab tab--edge tab--coral" style="right:40px;bottom:0"></span>
  </section>

</main>
</body>
</html>
```